Web Design Project for Karaoke Bar

This project is to redesign the clients current website. This is a karaoke bar in the Seattle downtown. Structure will remain the same. The "red-line" theme is a branded element along with the stick figure logo.
The would mostly like it updated to more modern looking site.
http://brambleloungekc.example/
We will want the contact information, including social media icons in the top right.
Social media integration of FB fan page is a must. Also a google map on the first page.
Target Market(s)
Mid 20's-30s, college students and professionals
Industry/Entity Type
Media
Look and feel

```html
<!DOCTYPE html>
<html lang="en">
<head>
<meta charset="utf-8">
<title>Bramble Lounge – Karaoke Bar</title>
<link href="https://fonts.googleapis.com/css2?family=Open+Sans:wght@400;600;700&family=PT+Sans:wght@400;700&display=swap" rel="stylesheet">
<style>
:root{
  --red-deep:#8e0b06;
  --red:#c9180c;
  --red-bright:#ff2a1a;
  --orange:#ff6a14;
  --tab:#e9e6dc;
  --black:#000;
  --footer:#1b1b1b;
  --white:#fff;
  --gold:#f2b712;
  --gold-dark:#c98a00;
  --text-muted:#cfcfcf;
}
*{box-sizing:border-box;margin:0;padding:0}
html,body{width:1000px;height:1200px;overflow:hidden;background:var(--black)}
body{font-family:"Open Sans",sans-serif;color:var(--white);position:relative}
a{text-decoration:none;color:inherit}
.abs{position:absolute}
.hero{left:0;top:0;width:1000px;height:600px;
  background:
   radial-gradient(ellipse 520px 260px at 500px 60px, rgba(255,90,40,.45), transparent 70%),
   linear-gradient(180deg, transparent 0, transparent 150px, rgba(255,60,20,.25) 170px, transparent 230px, transparent 270px, rgba(255,60,20,.22) 290px, transparent 340px),
   linear-gradient(180deg, var(--red) 0, #d4200e 300px, var(--red-deep) 520px, var(--black) 600px);}
.social{top:15px;left:771px;display:flex;gap:12px}
.social a{width:32px;height:32px;border-radius:5px;display:block}
.social .fb{background:#3b5ba8}.social .tw{background:#3fa6e4}.social .gp{background:#3a3a3a}.social .yt{background:#d8242a}
.brand{left:100px;top:58px;display:flex;align-items:center;gap:10px}
.brand-dot{width:80px;height:80px;border-radius:50%;background:var(--white)}
.brand-name{font-weight:700;font-size:22px;color:var(--white);line-height:1.1;width:110px}
.topnav{top:66px;left:0;width:1000px;height:30px;font-weight:600;font-size:19px}
.topnav a{position:absolute;top:0;color:var(--white);white-space:nowrap}
.redline-h{top:96px;left:300px;width:626px;height:3px;background:var(--red-bright);box-shadow:0 0 6px #ff5a4a}
.redline-v{top:232px;left:152px;width:3px;height:280px;background:var(--red-bright);box-shadow:0 0 6px #ff5a4a}
.banner{left:253px;top:143px;width:602px;height:80px;border:1px solid #888;
  background:linear-gradient(90deg,#3a3f48 0,#5a6270 55%,#2b3038 75%,#8a2a2a 85%,#404650 100%)}
.sidenav{top:248px;left:40px;width:101px;text-align:right;font-weight:600;font-size:20px;line-height:40px}
.sidenav a{display:block;color:var(--white)}
.section-title{font-weight:600;font-size:38px;letter-spacing:1.5px;line-height:1}
.announce-title{left:259px;top:239px}
.card{top:303px;width:165px}
.card .tab{width:91px;height:25px;background:var(--tab);color:#222;font-weight:600;font-size:15px;text-align:center;line-height:25px;border-radius:4px 4px 0 0;letter-spacing:.5px}
.card .photo{height:142px;background:radial-gradient(ellipse at 55% 55%,#8a5a35 0,#3a2316 35%,#101428 75%)}
.card .info{height:63px;background:var(--orange);padding:2px 7px}
.card .date{font-size:11px;color:#3a1500}
.card .name{font-weight:700;font-size:20px;line-height:21px;letter-spacing:.5px}
.arrow{top:412px}
.findus{left:74px;top:575px}
.map{left:74px;top:630px;width:267px;height:288px;background:linear-gradient(135deg,#eeeae2,#dcd8cf)}
.fanbox{left:436px;top:633px;width:210px;height:287px;background:var(--white);color:#333;padding:10px 8px;font-size:10px}
.fan-head{display:flex;gap:6px;align-items:flex-start}
.fan-sq{width:20px;height:20px;background:#e85a1c;flex:none;margin-top:3px}
.fan-org{color:#3b5998;font-weight:700;font-size:12px;line-height:14px}
.fan-org small{font-weight:400;font-size:9px}
.like{display:inline-block;margin:10px 0 0 18px;border:1px solid #aab;padding:2px 5px;color:#3b5998;font-size:10px;background:#eef}
.fan-count{border-top:1px solid #ddd;margin-top:8px;padding-top:8px;font-size:10px}
.fans{display:grid;grid-template-columns:repeat(4,44px);gap:6px 5px;margin-top:6px}
.fan .av{width:44px;height:44px;background:linear-gradient(#8a7a6c,#4c4038)}
.fan p{font-size:8px;color:#777;text-align:center;margin-top:6px}
.fan-foot{position:absolute;left:8px;right:8px;bottom:4px;border-top:1px solid #ddd;padding-top:3px;font-size:8px;color:#666}
.photos-title{left:729px;top:625px}
.pic{width:84px;height:94px;border:2px solid #f3d8e8;box-shadow:0 0 10px #ff8fc0;background:linear-gradient(160deg,#b88468,#3a2a30 60%,#2b3d8a)}
.btn{display:block;height:26px;border-radius:13px;background:linear-gradient(#ffd94a,var(--gold) 50%,var(--gold-dark));color:var(--white);font-weight:700;font-size:14px;text-align:center;line-height:24px;border:1px solid #8a6000}
.welcome{left:76px;top:950px}
.welcome-text{left:78px;top:991px;width:518px;font-family:"PT Sans",sans-serif;font-size:14.5px;line-height:18px;text-align:justify;color:var(--white)}
.flyer{top:955px;width:107px;height:145px;background:linear-gradient(#e7c530,#c9a21a)}
.footer{left:0;top:1131px;width:1000px;height:69px;background:var(--footer);text-align:center}
.footer p{font-size:14px;margin-top:14px}
.footer nav{font-size:11px;color:var(--text-muted);margin-top:2px}
</style>
</head>
<body>
<div class="abs hero"></div>

<nav class="abs social" aria-label="Social media">
  <a class="fb" href="#" aria-label="Fanpage"></a>
  <a class="tw" href="#" aria-label="Microblog"></a>
  <a class="gp" href="#" aria-label="Network"></a>
  <a class="yt" href="#" aria-label="Video channel"></a>
</nav>

<a class="abs brand" href="http://brambleloungekc.example/">
  <span class="brand-dot"></span>
  <span class="brand-name">Bramble Lounge</span>
</a>

<nav class="abs topnav">
  <a href="#" style="left:336px">Home</a>
  <a href="#" style="left:421px">Karaoke</a>
  <a href="#" style="left:525px">Sports</a>
  <a href="#" style="left:614px">Group Parties</a>
  <a href="#" style="left:766px">Pictures</a>
  <a href="#" style="left:868px">Bar</a>
</nav>
<div class="abs redline-h"></div>
<div class="abs redline-v"></div>

<div class="abs banner" role="img" aria-label="Promo banner: multiple large screens with football on TV"></div>

<nav class="abs sidenav">
  <a href="#">Home</a><a href="#">Menu</a><a href="#">Map</a><a href="#">Contact</a>
</nav>

<h2 class="abs section-title announce-title">Annoucements</h2>

<svg class="abs arrow" style="left:200px" width="34" height="47" viewBox="0 0 34 47"><path d="M32 2 L4 23.5 L32 45 L32 36 L16 23.5 L32 11Z" fill="#b40c08"/></svg>
<svg class="abs arrow" style="left:858px" width="34" height="47" viewBox="0 0 34 47"><path d="M2 2 L30 23.5 L2 45 L2 36 L18 23.5 L2 11Z" fill="#b40c08"/></svg>

<article class="abs card" style="left:256px">
  <div class="tab">Tuesday</div>
  <div class="photo" role="img" aria-label="Singer performing on stage"></div>
  <div class="info"><div class="date">25/05</div><div class="name">Lena Ruiz and Friends</div></div>
</article>
<article class="abs card" style="left:468px">
  <div class="tab">Tuesday</div>
  <div class="photo" role="img" aria-label="Singer performing on stage"></div>
  <div class="info"><div class="date">25/05</div><div class="name">Lena Ruiz and Friends</div></div>
</article>
<article class="abs card" style="left:679px;top:301px">
  <div class="tab">Tuesday</div>
  <div class="photo" role="img" aria-label="Singer performing on stage"></div>
  <div class="info"><div class="date">25/05</div><div class="name">Lena Ruiz and Friends</div></div>
</article>

<h2 class="abs section-title findus">Find Us :</h2>
<div class="abs map" role="img" aria-label="Street map showing the bar location"></div>

<aside class="abs fanbox">
  <div class="fan-head"><span class="fan-sq"></span><div class="fan-org">Northgate Media Co - Web Marketing Studio <small>on Fanpage</small></div></div>
  <span class="like">Like</span>
  <div class="fan-count">1,490 people like <b>Northgate Media Co - Web Marketing Studio.</b></div>
  <div class="fans">
    <div class="fan"><div class="av"></div><p>Mira</p></div>
    <div class="fan"><div class="av"></div><p>Ed</p></div>
    <div class="fan"><div class="av"></div><p>Jonah Reid</p></div>
    <div class="fan"><div class="av"></div><p>Colin</p></div>
    <div class="fan"><div class="av"></div><p>Tia</p></div>
    <div class="fan"><div class="av"></div><p>Rowan</p></div>
    <div class="fan"><div class="av"></div><p>Kai</p></div>
    <div class="fan"><div class="av"></div><p>Marisol</p></div>
  </div>
  <div class="fan-foot">Fanpage social plugin</div>
</aside>

<h2 class="abs section-title photos-title">Photos :</h2>
<div class="abs pic" style="left:730px;top:670px" role="img" aria-label="Guests posing at the bar"></div>
<div class="abs pic" style="left:834px;top:670px" role="img" aria-label="Guests posing at the bar"></div>
<div class="abs pic" style="left:730px;top:784px" role="img" aria-label="Guests posing at the bar"></div>
<div class="abs pic" style="left:834px;top:784px" role="img" aria-label="Guests posing at the bar"></div>
<a class="abs btn" style="left:724px;top:895px;width:94px" href="#">Read More</a>

<h2 class="abs section-title welcome">Welcome</h2>
<p class="abs welcome-text">Lorem ipsum dolor sit amet, consectetur adipiscing elit. Etiam vitae urna eu felis mtollis hendrerit non nec mi. Pellentesque nec velit non velit tincidunt lobortis ac sed elit sed elit. Donec sed velit nulla, Donec sed velit nulla vel elementum mi. Aliquam erat volutpat. Aliquam erat volutpat. Aliquam erat volutpat. Aliquam</p>
<a class="abs btn" style="left:76px;top:1075px;width:93px" href="#">Read More</a>

<div class="abs flyer" style="left:670px" role="img" aria-label="Happy hour menu flyer"></div>
<div class="abs flyer" style="left:817px" role="img" aria-label="Happy hour menu flyer"></div>

<footer class="abs footer">
  <p>Copyright 2012 - Bramble Lounge</p>
  <nav>Terms &amp; Conditions &nbsp;|&nbsp; Privacy Policy</nav>
</footer>
</body>
</html>
```